Business Card Design Project

Business Card
We are rebranding with a new logo
Industry/Entity Type
Business
Contact Information for Business Card
Dennis Marlow +61 427581962 dennis@qovo.com.au P.O. Box 872 Kelvindale QLD 4309
Requirements
Must have
- Logo

```html
<!DOCTYPE html>
<html lang="en">
<head>
<meta charset="utf-8">
<title>Qovo International – Business Card</title>
<link rel="stylesheet" href="https://fonts.googleapis.com/css2?family=Open+Sans:wght@400;600;700&display=swap">
<style>
  :root {
    --backdrop: #d9dbde;
    --card-white: #fbfbfb;
    --brand-blue: #0f86bd;
    --brand-blue-deep: #0a5f8a;
    --brand-blue-light: #2aa3d8;
    --brand-orange: #ef8123;
    --text-grey: #4a4a4a;
    --rule-grey: #a9a9a9;
  }
  * { box-sizing: border-box; margin: 0; padding: 0; }
  html, body { width: 1200px; height: 960px; overflow: hidden; }
  body {
    background: var(--backdrop);
    font-family: "Open Sans", Arial, sans-serif;
    display: flex;
    flex-direction: column;
    align-items: center;
    justify-content: center;
    gap: 30px;
  }
  .card {
    position: relative;
    width: 760px;
    height: 434px;
    overflow: hidden;
    box-shadow: 0 4px 14px rgba(0,0,0,0.18);
  }

  /* Back side */
  .card-back {
    background: radial-gradient(ellipse at 45% 35%, var(--brand-blue-light) 0%, var(--brand-blue) 45%, var(--brand-blue-deep) 100%);
    color: #ffffff;
    display: flex;
    flex-direction: column;
    align-items: center;
    justify-content: center;
  }
  .back-wordmark {
    font-size: 54px;
    font-weight: 600;
    letter-spacing: 1px;
    line-height: 1;
  }
  .back-tagline {
    margin-top: 14px;
    font-size: 26px;
    font-weight: 600;
    letter-spacing: 5px;
  }
  .back-url {
    margin-top: 26px;
    font-size: 14px;
    letter-spacing: 5px;
    opacity: 0.85;
  }

  /* Front side */
  .card-front { background: var(--card-white); }
  .front-logo {
    position: absolute;
    top: 120px;
    right: 62px;
    text-align: right;
    color: var(--brand-blue);
    font-weight: 600;
    line-height: 1;
  }
  .front-logo .logo-name { font-size: 44px; }
  .front-logo .logo-sub { display: block; margin-top: 8px; font-size: 19px; letter-spacing: 3px; }
  .holder-name {
    position: absolute;
    top: 168px;
    left: 58px;
    color: var(--brand-blue);
    font-size: 17px;
    font-weight: 700;
    text-transform: uppercase;
  }
  .name-rule {
    position: absolute;
    top: 200px;
    left: 56px;
    width: 650px;
    height: 1px;
    background: var(--rule-grey);
  }
  .contact-list {
    position: absolute;
    top: 210px;
    left: 58px;
    list-style: none;
    color: var(--text-grey);
    font-size: 15px;
    line-height: 24px;
  }
  .contact-list li { display: flex; align-items: center; gap: 10px; }
  .contact-list svg { width: 13px; height: 13px; fill: var(--brand-blue); flex: none; }
  .address {
    position: absolute;
    right: 62px;
    bottom: 52px;
    text-align: right;
    color: var(--text-grey);
    font-size: 16px;
    line-height: 22px;
  }
  .address-rule {
    position: absolute;
    bottom: 112px;
    right: 56px;
    width: 460px;
    height: 1px;
    background: var(--rule-grey);
  }
  .edge-band {
    position: absolute;
    left: 0; right: 0; bottom: 0;
    height: 16px;
    background: var(--brand-blue);
    border-top: 4px solid var(--brand-orange);
  }
</style>
</head>
<body>
  <section class="card card-back" aria-label="Card back">
    <div class="back-wordmark">Qovo</div>
    <div class="back-tagline">INTERNATIONAL</div>
    <div class="back-url">www.qovo.com.au</div>
  </section>

  <section class="card card-front" aria-label="Card front">
    <div class="front-logo">
      <span class="logo-name">Qovo</span>
      <span class="logo-sub">INTERNATIONAL</span>
    </div>

    <h1 class="holder-name">Dennis Marlow</h1>
    <div class="name-rule"></div>

    <ul class="contact-list">
      <li>
        <svg viewBox="0 0 16 16" aria-hidden="true"><path d="M3 1h3l1.5 4-2 1.3a9 9 0 0 0 4.2 4.2L11 8.5 15 10v3a2 2 0 0 1-2 2A12 12 0 0 1 1 3a2 2 0 0 1 2-2z"/></svg>
        +61 427581962
      </li>
      <li>
        <svg viewBox="0 0 16 16" aria-hidden="true"><path d="M1 3h14v10H1z M1 3l7 6 7-6" stroke="#fbfbfb" stroke-width="1.2"/></svg>
        dennis@qovo.com.au
      </li>
      <li>
        <svg viewBox="0 0 16 16" aria-hidden="true"><circle cx="8" cy="8" r="7"/><path d="M1 8h14M8 1c-3 3-3 11 0 14M8 1c3 3 3 11 0 14" stroke="#fbfbfb" stroke-width="1" fill="none"/></svg>
        www.qovo.com.au
      </li>
    </ul>

    <div class="address-rule"></div>
    <address class="address" style="font-style: normal;">
      P.O. Box 872<br>Kelvindale QLD 4309
    </address>

    <div class="edge-band"></div>
  </section>
</body>
</html>
```